PowerPoint Template - Multiple Slide Backgrounds

Looking for a professional PowerPoint template for a technology company. You will see with the logo there's sort of a theme with gears and a lightbulb of sorts. Keeping with this sort of design could help with the brand.

Branding information
• Logo with transparent background included
• Primary Color (Orange) Hex #E6753D
• Secondary Color (Brown) Hex #6A4238
• Primary Font - Myriad Pro
• Secondary Font - Quiet Sans Light

Design request -
• PowerPoint (POTX) template with master slide views
• Cover Slide
• Color Pallet - 7 Color PowerPoint pallet that includes and complements primary and secondary colors
• Slide Master with Footer
• Multiple Background Types to allow for smart art overlay or bullet point text boxes
Bonus - Sample graphical elements using shapes and smart art

```html
<!DOCTYPE html>
<html lang="en">
<head>
<meta charset="utf-8">
<title>Northfield DevWorks – PowerPoint Template</title>
<link href="https://fonts.googleapis.com/css2?family=Source+Sans+3:wght@400;600;700&display=swap" rel="stylesheet">
<style>
:root{
  --teal:#4FAAB8;
  --orange:#E6753D;
  --brown:#6A4238;
  --ink:#333333;
  --muted:#777777;
  --gray:#A6A6A6;
  --line:#D6D6D6;
  --blue:#4A7CC9;
  --sky:#5B9BD5;
  --yellow:#F2C12E;
  --white:#FFFFFF;
}
*{box-sizing:border-box;margin:0;padding:0}
html,body{width:1200px;height:3564px;overflow:hidden}
body{position:relative;background:var(--teal);font-family:"Source Sans 3",Arial,sans-serif;color:var(--ink)}
.slide{position:absolute;width:520px;height:292px;background:var(--white);overflow:hidden;box-shadow:0 1px 3px rgba(0,0,0,.15)}
.abs{position:absolute}
.section-heading{position:absolute;top:666px;left:0;width:1200px;text-align:center;color:var(--white);font-size:34px;font-weight:400;letter-spacing:.3px}
.title{position:absolute;top:14px;left:0;width:100%;text-align:center;font-size:21px;font-weight:700;color:var(--brown)}
.subtitle{position:absolute;top:42px;left:0;width:100%;text-align:center;font-size:7.5px;color:var(--ink)}
.subtitle em{font-style:normal;color:var(--orange)}
.dots{position:absolute;top:55px;left:0;width:100%;display:flex;justify-content:center;gap:3px}
.dots i{display:block;width:4px;height:4px;border-radius:50%;background:var(--orange)}
.copy{font-size:7px;line-height:1.38;color:var(--ink)}
.copy-sm{font-size:6.3px;line-height:1.38;color:var(--ink)}
.label{font-size:7px;font-weight:700;color:var(--brown);letter-spacing:.3px}
.foot-brand{position:absolute;left:12px;bottom:8px;display:flex;align-items:center;gap:4px}
.foot-mark{width:10px;height:10px;border-radius:50%;border:2px solid var(--orange)}
.foot-name{font-size:7.5px;font-weight:700;color:var(--brown)}
.foot-rule{position:absolute;left:100px;right:28px;bottom:12px;height:1px;background:var(--brown);opacity:.6}
.foot-home{position:absolute;right:10px;bottom:8px;width:12px;height:11px}
.foot-band{position:absolute;left:0;right:0;bottom:0;height:13px;background:var(--brown)}
.brand-word{font-weight:700;color:var(--orange);white-space:nowrap}
.feature{position:absolute;width:112px}
.feature svg{display:block;margin:0 auto 4px;width:13px;height:13px}
.feature h4{font-size:6.5px;font-weight:700;color:var(--brown);margin-bottom:2px}
.agenda-list{position:absolute;left:230px;top:22px;width:255px;list-style:none}
.agenda-list li{display:flex;font-size:7.5px;color:var(--ink);height:20.5px;align-items:center;border-bottom:1px solid var(--line)}
.agenda-list b{width:38px;font-weight:400}
.bar{position:absolute;height:24px;display:flex;align-items:center;color:var(--white);font-size:8px;font-weight:700}
.pct{position:absolute;width:22px;height:22px;border-radius:50%;background:var(--white);border:2px solid;font-size:6px;display:flex;align-items:center;justify-content:center;color:var(--ink);font-weight:600}
.num{position:absolute;width:22px;height:22px;border-radius:50%;color:var(--white);font-size:10px;font-weight:700;display:flex;align-items:center;justify-content:center}
.contact-item{position:absolute;width:100px;text-align:center}
.contact-item .dot{width:22px;height:22px;border-radius:50%;margin:0 auto 6px}
.contact-item p{font-size:6.5px;font-weight:700;color:var(--brown);letter-spacing:.3px;border-bottom:1px solid var(--line);padding-bottom:2px;display:inline-block}
.info-item{position:absolute;width:90px;text-align:center;font-size:6.3px;color:var(--ink)}
.info-item svg{display:block;margin:0 auto 4px;width:11px;height:11px}
.gear-spot{position:absolute;top:145px;width:64px;height:64px;border-radius:50%}
</style>
</head>
<body>

<section class="slide cover-plain" style="top:43px;left:45px">
  <div class="abs" style="top:100px;left:0;width:100%;display:flex;justify-content:center;align-items:center;gap:10px">
    <span style="width:34px;height:34px;border-radius:50%;border:5px solid var(--brown)"></span>
    <span class="brand-word" style="font-size:30px">Northfield DevWorks</span>
  </div>
  <div class="abs" style="left:0;right:0;bottom:16px;height:2px;background:var(--orange)"></div>
  <div class="abs" style="left:0;right:0;bottom:0;height:12px;background:var(--brown)"></div>
</section>

<section class="slide cover-desk" style="top:43px;left:635px">
  <div class="abs" role="img" aria-label="Photo of a bright desk with a monitor, lamp and teapot" style="inset:0;background:linear-gradient(180deg,#f7f7f7 0%,#e8e8e8 60%,#d9d9d9 100%)"></div>
  <div class="abs" style="top:62px;left:175px;width:175px;height:118px;background:#fdfdfd;display:flex;align-items:center;justify-content:center">
    <span class="brand-word" style="font-size:15px">Northfield DevWorks</span>
  </div>
</section>

<section class="slide cover-bulb" style="top:356px;left:45px">
  <div class="abs" role="img" aria-label="Dark photo of a light bulb lying on a table" style="inset:0;background:radial-gradient(ellipse at 35% 80%,#6b6b6b 0%,#2a2a2a 45%,#0f0f0f 100%)"></div>
  <div class="abs" style="top:0;left:120px;width:285px;height:165px;background:rgba(205,205,205,.72);display:flex;align-items:center;justify-content:center">
    <span class="brand-word" style="font-size:20px">Northfield DevWorks</span>
  </div>
</section>

<section class="slide cover-keys" style="top:356px;left:635px">
  <div class="abs" role="img" aria-label="Close photo of a backlit keyboard in blue tones" style="top:20px;left:14px;right:14px;bottom:40px;background:linear-gradient(135deg,#1c2a4a 0%,#2f4e86 40%,#12182c 75%,#3b2b3a 100%)"></div>
  <div class="abs" style="top:85px;left:75px;width:130px;height:130px;border-radius:50%;background:var(--white);display:flex;align-items:center;justify-content:center;text-align:center">
    <span class="brand-word" style="font-size:14px;white-space:normal;line-height:1.1">Northfield<br>DevWorks</span>
  </div>
</section>

<h1 class="section-heading">Slide Master with 3 different Footer</h1>

<section class="slide master-a" style="top:725px;left:45px">
  <h2 class="title">Lorem ipsum dolor sit</h2>
  <p class="subtitle">Your great subtitle <em>goes here</em></p>
  <div class="dots"><i></i><i></i><i></i></div>
  <div class="abs" role="img" aria-label="Orange light bulb illustration with rays" style="top:95px;left:75px;width:90px;height:100px;border-radius:45px 45px 20px 20px;background:radial-gradient(circle at 45% 40%,#F29A66,var(--orange))"></div>
  <div class="feature" style="left:255px;top:78px"><svg viewBox="0 0 12 12"><path d="M2 10l6-6 2 2-6 6H2z" fill="none" stroke="#666"/></svg><h4>YOUR TITLE HERE</h4><p class="copy-sm">Lorem ipsum dolor sit amet, consectetur adipiscing elit, sed do eiusmod tempor.</p></div>
  <div class="feature" style="left:385px;top:78px"><svg viewBox="0 0 12 12"><rect x="2" y="5" width="8" height="6" fill="none" stroke="#666"/><path d="M4 5V3a2 2 0 014 0v2" fill="none" stroke="#666"/></svg><h4>YOUR TITLE HERE</h4><p class="copy-sm">Lorem ipsum dolor sit amet, consectetur adipiscing elit, sed do eiusmod tempor.</p></div>
  <div class="feature" style="left:255px;top:165px"><svg viewBox="0 0 12 12"><circle cx="6" cy="6" r="5" fill="none" stroke="#666"/><path d="M1 6h10M6 1v10" stroke="#666"/></svg><h4>YOUR TITLE HERE</h4><p class="copy-sm">Lorem ipsum dolor sit amet, consectetur adipiscing elit, sed do eiusmod tempor.</p></div>
  <div class="feature" style="left:385px;top:165px"><svg viewBox="0 0 12 12"><rect x="1" y="4" width="7" height="5" fill="none" stroke="#666"/><path d="M8 6h2l1 2v1H8" fill="none" stroke="#666"/></svg><h4>YOUR TITLE HERE</h4><p class="copy-sm">Lorem ipsum dolor sit amet, consectetur adipiscing elit, sed do eiusmod tempor.</p></div>
  <div class="foot-brand"><span class="foot-mark"></span><span class="foot-name">Northfield DevWorks</span></div>
  <svg class="foot-home" viewBox="0 0 12 11"><path d="M0 5L6 0l6 5v6H0z" fill="var(--brown)"/></svg>
</section>

<section class="slide master-b" style="top:725px;left:635px">
  <h2 class="title">Lorem ipsum dolor sit</h2>
  <p class="subtitle">Your great subtitle <em>goes here</em></p>
  <div class="dots"><i></i><i></i><i></i></div>
  <div class="abs" role="img" aria-label="Orange light bulb illustration with rays" style="top:95px;left:75px;width:90px;height:100px;border-radius:45px 45px 20px 20px;background:radial-gradient(circle at 45% 40%,#F29A66,var(--orange))"></div>
  <div class="feature" style="left:255px;top:78px"><svg viewBox="0 0 12 12"><path d="M2 10l6-6 2 2-6 6H2z" fill="none" stroke="#666"/></svg><h4>YOUR TITLE HERE</h4><p class="copy-sm">Lorem ipsum dolor sit amet, consectetur adipiscing elit, sed do eiusmod tempor.</p></div>
  <div class="feature" style="left:385px;top:78px"><svg viewBox="0 0 12 12"><rect x="2" y="5" width="8" height="6" fill="none" stroke="#666"/><path d="M4 5V3a2 2 0 014 0v2" fill="none" stroke="#666"/></svg><h4>YOUR TITLE HERE</h4><p class="copy-sm">Lorem ipsum dolor sit amet, consectetur adipiscing elit, sed do eiusmod tempor.</p></div>
  <div class="feature" style="left:255px;top:165px"><svg viewBox="0 0 12 12"><circle cx="6" cy="6" r="5" fill="none" stroke="#666"/><path d="M1 6h10M6 1v10" stroke="#666"/></svg><h4>YOUR TITLE HERE</h4><p class="copy-sm">Lorem ipsum dolor sit amet, consectetur adipiscing elit, sed do eiusmod tempor.</p></div>
  <div class="feature" style="left:385px;top:165px"><svg viewBox="0 0 12 12"><rect x="1" y="4" width="7" height="5" fill="none" stroke="#666"/><path d="M8 6h2l1 2v1H8" fill="none" stroke="#666"/></svg><h4>YOUR TITLE HERE</h4><p class="copy-sm">Lorem ipsum dolor sit amet, consectetur adipiscing elit, sed do eiusmod tempor.</p></div>
  <div class="foot-band"></div>
  <svg class="foot-home" viewBox="0 0 12 11" style="bottom:16px"><path d="M0 5L6 0l6 5v6H0z" fill="var(--brown)"/></svg>
</section>

<section class="slide master-c" style="top:1041px;left:340px">
  <h2 class="title">Lorem ipsum dolor sit</h2>
  <p class="subtitle">Your great subtitle <em>goes here</em></p>
  <div class="dots"><i></i><i></i><i></i></div>
  <div class="abs" role="img" aria-label="Orange light bulb illustration with rays" style="top:95px;left:75px;width:90px;height:100px;border-radius:45px 45px 20px 20px;background:radial-gradient(circle at 45% 40%,#F29A66,var(--orange))"></div>
  <div class="feature" style="left:255px;top:78px"><svg viewBox="0 0 12 12"><path d="M2 10l6-6 2 2-6 6H2z" fill="none" stroke="#666"/></svg><h4>YOUR TITLE HERE</h4><p class="copy-sm">Lorem ipsum dolor sit amet, consectetur adipiscing elit, sed do eiusmod tempor.</p></div>
  <div class="feature" style="left:385px;top:78px"><svg viewBox="0 0 12 12"><rect x="2" y="5" width="8" height="6" fill="none" stroke="#666"/><path d="M4 5V3a2 2 0 014 0v2" fill="none" stroke="#666"/></svg><h4>YOUR TITLE HERE</h4><p class="copy-sm">Lorem ipsum dolor sit amet, consectetur adipiscing elit, sed do eiusmod tempor.</p></div>
  <div class="feature" style="left:255px;top:160px"><svg viewBox="0 0 12 12"><circle cx="6" cy="6" r="5" fill="none" stroke="#666"/><path d="M1 6h10M6 1v10" stroke="#666"/></svg><h4>YOUR TITLE HERE</h4><p class="copy-sm">Lorem ipsum dolor sit amet, consectetur adipiscing elit, sed do eiusmod tempor.</p></div>
  <div class="feature" style="left:385px;top:160px"><svg viewBox="0 0 12 12"><rect x="1" y="4" width="7" height="5" fill="none" stroke="#666"/><path d="M8 6h2l1 2v1H8" fill="none" stroke="#666"/></svg><h4>YOUR TITLE HERE</h4><p class="copy-sm">Lorem ipsum dolor sit amet, consectetur adipiscing elit, sed do eiusmod tempor.</p></div>
  <svg class="abs" style="left:0;bottom:0" width="520" height="28" viewBox="0 0 520 28"><path d="M95 6H520V28H80z" fill="var(--brown)"/><path d="M440 0H520V28H425z" fill="var(--orange)"/></svg>
  <div class="foot-brand"><span class="foot-mark"></span><span class="foot-name">Northfield DevWorks</span></div>
</section>

<section class="slide agenda" style="top:1366px;left:45px">
  <h2 class="abs" style="top:122px;left:30px;font-size:19px;font-weight:700;color:var(--brown)">Agenda</h2>
  <p class="abs" style="top:146px;left:30px;font-size:6.5px">Your great subtitle <span style="color:var(--orange)">goes here</span></p>
  <div class="abs" style="top:157px;left:30px;display:flex;gap:3px"><i style="width:4px;height:4px;border-radius:50%;background:var(--orange)"></i><i style="width:4px;height:4px;border-radius:50%;background:var(--orange)"></i><i style="width:4px;height:4px;border-radius:50%;background:var(--orange)"></i></div>
  <ol class="agenda-list">
    <li><b>i.</b>Introduction</li><li><b>ii.</b>About Us</li><li><b>iii.</b>Welcome Message</li><li><b>iv.</b>Company Profile</li><li><b>v.</b>Team</li><li><b>vi.</b>Team Group</li><li><b>vii.</b>Portfolio</li><li><b>viii.</b>Info graphic</li><li><b>ix.</b>Contact Us</li><li><b>x.</b>Data Chart</li>
  </ol>
  <div class="foot-brand"><span class="foot-mark"></span><span class="foot-name">Northfield DevWorks</span></div>
  <div class="foot-rule"></div>
  <svg class="foot-home" viewBox="0 0 12 11"><path d="M0 5L6 0l6 5v6H0z" fill="var(--brown)"/></svg>
</section>

<section class="slide cycle" style="top:1366px;left:635px">
  <h2 class="title">Cycle Infographic</h2>
  <p class="subtitle">Your great subtitle <em>goes here</em></p>
  <div class="dots"><i></i><i></i><i></i></div>
  <svg class="abs" style="top:95px;left:195px" width="130" height="130" viewBox="0 0 130 130">
    <g fill="none" stroke-width="30">
      <circle cx="65" cy="65" r="48" stroke="var(--orange)" stroke-dasharray="70 232" transform="rotate(-88 65 65)"/>
      <circle cx="65" cy="65" r="48" stroke="var(--gray)" stroke-dasharray="70 232" transform="rotate(2 65 65)"/>
      <circle cx="65" cy="65" r="48" stroke="var(--blue)" stroke-dasharray="70 232" transform="rotate(92 65 65)"/>
      <circle cx="65" cy="65" r="48" stroke="var(--sky)" stroke-dasharray="70 232" transform="rotate(182 65 65)"/>
    </g>
  </svg>
  <p class="copy abs" style="top:95px;left:28px;width:150px">Lorem ipsum dolor sit amet, consectetur adipiscing elit, sed do eiusmod tempor incididunt ut labore et dolore magna aliqua. Ut enim ad minim veniam, quis nostrud.</p>
  <p class="copy abs" style="top:185px;left:28px;width:150px">Lorem ipsum dolor sit amet, consectetur adipiscing elit, sed do eiusmod tempor incididunt ut labore et dolore magna aliqua. Ut enim ad minim veniam, quis nostrud.</p>
  <p class="copy abs" style="top:95px;left:345px;width:150px">Lorem ipsum dolor sit amet, consectetur adipiscing elit, sed do eiusmod tempor incididunt ut labore et dolore magna aliqua. Ut enim ad minim veniam, quis nostrud.</p>
  <p class="copy abs" style="top:185px;left:345px;width:150px">Lorem ipsum dolor sit amet, consectetur adipiscing elit, sed do eiusmod tempor incididunt ut labore et dolore magna aliqua. Ut enim ad minim veniam, quis nostrud.</p>
  <div class="foot-brand"><span class="foot-mark"></span><span class="foot-name">Northfield DevWorks</span></div>
  <div class="foot-rule"></div>
  <svg class="foot-home" viewBox="0 0 12 11"><path d="M0 5L6 0l6 5v6H0z" fill="var(--brown)"/></svg>
</section>

<section class="slide two-columns" style="top:1687px;left:45px">
  <div class="abs" role="img" aria-label="Misty grey landscape photo" style="top:0;left:0;right:0;height:118px;background:linear-gradient(180deg,#ffffff 0%,#e4e4e4 45%,#a9a9a9 100%)"></div>
  <h2 class="title">Two columns text and picture</h2>
  <p class="subtitle">Your great subtitle <em>goes here</em></p>
  <div class="dots"><i></i><i></i><i></i></div>
  <p class="copy abs" style="top:135px;left:28px;width:215px">Lorem ipsum dolor sit amet, consectetur adipiscing elit, sed do eiusmod tempor incididunt ut labore et dolore magna aliqua. Ut enim ad minim veniam, quis nostrud exercitation ullamco laboris nisi ut aliquip ex ea commodo consequat.</p>
  <p class="copy abs" style="top:135px;left:277px;width:215px">Lorem ipsum dolor sit amet, consectetur adipiscing elit, sed do eiusmod tempor incididunt ut labore et dolore magna aliqua. Ut enim ad minim veniam, quis nostrud exercitation ullamco laboris nisi ut aliquip ex ea commodo consequat.</p>
  <div class="foot-brand"><span class="foot-mark"></span><span class="foot-name">Northfield DevWorks</span></div>
  <div class="foot-rule"></div>
  <svg class="foot-home" viewBox="0 0 12 11"><path d="M0 5L6 0l6 5v6H0z" fill="var(--brown)"/></svg>
</section>

<section class="slide swot" style="top:1687px;left:635px">
  <h2 class="title">SWOT analyses</h2>
  <p class="subtitle">Your great subtitle <em>goes here</em></p>
  <div class="dots"><i></i><i></i><i></i></div>
  <div class="abs" style="top:80px;left:258px;width:1px;height:180px;background:var(--line)"></div>
  <div class="abs" style="top:170px;left:25px;width:470px;height:1px;background:var(--line)"></div>
  <div class="abs" style="top:148px;left:237px;width:44px;height:44px;border-radius:50%;background:var(--orange);color:#fff;font-size:8px;font-weight:700;display:flex;align-items:center;justify-content:center">SWOT</div>
  <p class="abs" style="top:88px;left:90px;font-size:7px;font-weight:700;color:var(--blue)">STRENGTH</p>
  <p class="copy abs" style="top:100px;left:25px;width:210px">Lorem ipsum dolor sit amet, consectetur adipiscing elit, sed do eiusmod tempor incididunt ut labore et dolore magna aliqua. Ut enim ad minim veniam.</p>
  <p class="abs" style="top:88px;left:400px;font-size:7px;font-weight:700;color:var(--orange)">WEAKNESS</p>
  <p class="copy abs" style="top:100px;left:285px;width:210px">Lorem ipsum dolor sit amet, consectetur adipiscing elit, sed do eiusmod tempor incididunt ut labore et dolore magna aliqua. Ut enim ad minim veniam.</p>
  <p class="abs" style="top:196px;left:80px;font-size:7px;font-weight:700;color:var(--gray)">OPPORTUNITIES</p>
  <p class="copy abs" style="top:208px;left:25px;width:210px">Lorem ipsum dolor sit amet, consectetur adipiscing elit, sed do eiusmod tempor incididunt ut labore et dolore magna aliqua. Ut enim ad minim veniam.</p>
  <p class="abs" style="top:196px;left:410px;font-size:7px;font-weight:700;color:var(--yellow)">THREATS</p>
  <p class="copy abs" style="top:208px;left:285px;width:210px">Lorem ipsum dolor sit amet, consectetur adipiscing elit, sed do eiusmod tempor incididunt ut labore et dolore magna aliqua. Ut enim ad minim veniam.</p>
  <div class="foot-brand"><span class="foot-mark"></span><span class="foot-name">Northfield DevWorks</span></div>
  <div class="foot-rule"></div>
  <svg class="foot-home" viewBox="0 0 12 11"><path d="M0 5L6 0l6 5v6H0z" fill="var(--brown)"/></svg>
</section>

<section class="slide hexagons" style="top:2008px;left:45px">
  <h2 class="abs" style="top:45px;left:25px;width:140px;font-size:19px;line-height:1.05;font-weight:700;color:var(--brown)">Lorem ipsum dolor sit amet</h2>
  <div class="abs" style="top:115px;left:25px;display:flex;gap:3px"><i style="width:4px;height:4px;border-radius:50%;background:var(--orange)"></i><i style="width:4px;height:4px;border-radius:50%;background:var(--orange)"></i><i style="width:4px;height:4px;border-radius:50%;background:var(--orange)"></i></div>
  <p class="copy abs" style="top:126px;left:25px;width:130px">Lorem ipsum dolor sit amet, consectetur adipiscing elit, sed do eiusmod tempor incididunt ut labore et dolore magna aliqua. Ut enim ad minim veniam, quis nostrud exercitation ullamco laboris nisi ut aliquip ex ea commodo consequat.</p>
  <svg class="abs" style="top:30px;left:200px" width="260" height="230" viewBox="0 0 260 230" font-family="Source Sans 3, Arial, sans-serif" font-size="6.5" fill="#fff" text-anchor="middle">
    <defs><polygon id="hex" points="0,-34 29.4,-17 29.4,17 0,34 -29.4,17 -29.4,-17"/></defs>
    <use href="#hex" x="130" y="115" fill="var(--brown)"/>
    <use href="#hex" x="189" y="115" fill="var(--orange)"/><text x="189" y="113">Multiple</text><text x="189" y="121">Locations</text>
    <use href="#hex" x="159.5" y="166" fill="var(--orange)"/><text x="159.5" y="168">Cost Effective</text>
    <use href="#hex" x="100.5" y="166" fill="var(--orange)"/><text x="100.5" y="168">Time Saver</text>
    <use href="#hex" x="71" y="115" fill="var(--orange)"/><text x="71" y="117">Social Media</text>
    <use href="#hex" x="100.5" y="64" fill="var(--orange)"/><text x="100.5" y="66">Video Calls</text>
    <use href="#hex" x="159.5" y="64" fill="var(--orange)"/><text x="159.5" y="66">Cloud Drives</text>
  </svg>
  <div class="foot-brand"><span class="foot-mark"></span><span class="foot-name">Northfield DevWorks</span></div>
  <div class="foot-rule"></div>
  <svg class="foot-home" viewBox="0 0 12 11"><path d="M0 5L6 0l6 5v6H0z" fill="var(--brown)"/></svg>
</section>

<section class="slide orange-panel" style="top:2008px;left:635px">
  <div class="abs" style="top:0;left:0;width:155px;height:100%;background:linear-gradient(180deg,var(--orange) 0%,#B0593A 60%,var(--brown) 100%);display:flex;align-items:center;justify-content:center;padding:0 16px">
    <p style="font-size:7.5px;line-height:1.4;color:#fff;text-align:center">Lorem ipsum dolor sit amet, consectetur adipiscing elit, sed do eiusmod tempor incididunt ut labore et dolore magna aliqua. Ut enim ad minim veniam, quis nostrud exercitation ullamco laboris nisi ut aliquip ex ea commodo consequat.</p>
  </div>
  <svg class="abs" style="top:40px;left:232px" width="18" height="16" viewBox="0 0 18 16"><rect x="1" y="1" width="16" height="12" fill="none" stroke="var(--orange)" stroke-width="1.5"/><path d="M4 10l3-4 3 3 4-5" fill="none" stroke="var(--orange)" stroke-width="1.5"/></svg>
  <svg class="abs" style="top:40px;left:390px" width="18" height="16" viewBox="0 0 18 16"><path d="M2 14V9M6 14V6M10 14V8M14 14V3" stroke="var(--orange)" stroke-width="2"/></svg>
  <p class="label abs" style="top:62px;left:205px;width:70px;text-align:center">LOREM IPSUM</p>
  <p class="label abs" style="top:62px;left:364px;width:70px;text-align:center">LOREM IPSUM</p>
  <p class="copy abs" style="top:80px;left:172px;width:140px">Lorem ipsum dolor sit amet, consectetur adipiscing elit, sed do eiusmod tempor incididunt ut labore et dolore magna aliqua. Ut enim ad minim veniam, quis nostrud exercitation ullamco laboris nisi ut aliquip ex ea commodo consequat.</p>
  <p class="copy abs" style="top:80px;left:330px;width:140px">Lorem ipsum dolor sit amet, consectetur adipiscing elit, sed do eiusmod tempor incididunt ut labore et dolore magna aliqua. Ut enim ad minim veniam, quis nostrud exercitation ullamco laboris nisi ut aliquip ex ea commodo consequat.</p>
  <div class="abs" style="left:175px;right:28px;bottom:12px;height:1px;background:var(--brown);opacity:.6"></div>
  <svg class="foot-home" viewBox="0 0 12 11"><path d="M0 5L6 0l6 5v6H0z" fill="var(--brown)"/></svg>
</section>

<section class="slide magnifier" style="top:2324px;left:45px">
  <div class="bar" style="top:38px;left:0;width:215px;background:var(--blue);border-radius:0 12px 12px 0;padding-left:60px">First Title #1</div>
  <div class="pct" style="top:39px;left:22px;border-color:var(--blue)">50%</div>
  <div class="bar" style="top:88px;left:30px;width:185px;background:var(--orange);border-radius:12px;padding-left:62px">Second Title #2</div>
  <div class="pct" style="top:89px;left:52px;border-color:var(--orange)">50%</div>
  <div class="bar" style="top:138px;left:60px;width:165px;background:var(--brown);border-radius:12px;padding-left:70px">Third Title #3</div>
  <div class="pct" style="top:139px;left:82px;border-color:var(--brown)">50%</div>
  <div class="bar" style="top:38px;right:0;width:215px;background:var(--blue);border-radius:12px 0 0 12px;padding-left:80px">First Title #1</div>
  <div class="pct" style="top:39px;right:22px;border-color:var(--blue)">50%</div>
  <div class="bar" style="top:88px;right:30px;width:185px;background:var(--orange);border-radius:12px;padding-left:70px">Second Title #2</div>
  <div class="pct" style="top:89px;right:52px;border-color:var(--orange)">50%</div>
  <div class="bar" style="top:138px;right:60px;width:165px;background:var(--brown);border-radius:12px;padding-left:64px">Third Title #3</div>
  <div class="pct" style="top:139px;right:82px;border-color:var(--brown)">50%</div>
  <div class="abs" role="img" aria-label="Magnifying glass illustration in grey tones" style="top:30px;left:198px;width:124px;height:250px;border-radius:62px 62px 10px 10px;background:linear-gradient(180deg,#E3E3E3 0%,#C9C9C9 50%,#5A5A5A 100%)"></div>
  <p class="abs" style="top:86px;left:198px;width:124px;text-align:center;font-size:10px;font-weight:700;color:var(--ink)">Main Title</p>
</section>

<section class="slide numbered" style="top:2324px;left:635px">
  <div class="abs" style="top:120px;left:35px;display:flex;align-items:center;gap:6px">
    <span style="width:20px;height:20px;border-radius:50%;border:4px solid var(--brown)"></span>
    <span class="brand-word" style="font-size:16px">Northfield DevWorks</span>
  </div>
  <div class="num" style="top:22px;left:260px;background:var(--sky)">1</div>
  <p class="copy abs" style="top:24px;left:292px;width:205px">Lorem ipsum dolor sit amet, consectetur adipiscing elit, sed do eiusmod tempor incididunt ut labore et dolore magna aliqua.</p>
  <div class="num" style="top:85px;left:260px;background:var(--orange)">2</div>
  <p class="copy abs" style="top:87px;left:292px;width:205px">Lorem ipsum dolor sit amet, consectetur adipiscing elit, sed do eiusmod tempor incididunt ut labore et dolore magna aliqua.</p>
  <div class="num" style="top:148px;left:260px;background:var(--gray)">3</div>
  <p class="copy abs" style="top:150px;left:292px;width:205px">Lorem ipsum dolor sit amet, consectetur adipiscing elit, sed do eiusmod tempor incididunt ut labore et dolore magna aliqua.</p>
  <div class="num" style="top:211px;left:260px;background:var(--yellow)">4</div>
  <p class="copy abs" style="top:213px;left:292px;width:205px">Lorem ipsum dolor sit amet, consectetur adipiscing elit, sed do eiusmod tempor incididunt ut labore et dolore magna aliqua.</p>
  <div class="abs" style="left:0;right:0;bottom:12px;height:1px;background:var(--brown);opacity:.6"></div>
</section>

<section class="slide text-columns" style="top:2645px;left:45px">
  <h2 class="title">Lorem ipsum dolor sit</h2>
  <p class="subtitle">Your great subtitle <em>goes here</em></p>
  <div class="dots"><i></i><i></i><i></i></div>
  <p class="copy abs" style="top:80px;left:28px;width:140px">Lorem ipsum dolor sit amet, consectetur adipiscing elit, sed do eiusmod tempor incididunt ut labore et dolore magna aliqua. Ut enim ad minim veniam, quis nostrud exercitation.<br><br>Duis aute irure dolor in reprehenderit in voluptate velit esse cillum dolore eu fugiat nulla pariatur. Excepteur sint occaecat cupidatat non proident.</p>
  <p class="copy abs" style="top:80px;left:190px;width:140px">Lorem ipsum dolor sit amet, consectetur adipiscing elit, sed do eiusmod tempor incididunt ut labore et dolore magna aliqua. Ut enim ad minim veniam, quis nostrud.<br><br>Occaecat cupidatat non proident, sunt in culpa qui officia deserunt mollit anim id est laborum.</p>
  <p class="copy abs" style="top:80px;left:352px;width:140px">Lorem ipsum dolor sit amet, consectetur adipiscing elit, sed do eiusmod tempor incididunt ut labore et dolore magna aliqua. Ut enim ad minim veniam, quis nostrud exercitation.</p>
  <div class="foot-brand"><span class="foot-mark"></span><span class="foot-name">Northfield DevWorks</span></div>
  <div class="foot-rule"></div>
  <svg class="foot-home" viewBox="0 0 12 11"><path d="M0 5L6 0l6 5v6H0z" fill="var(--brown)"/></svg>
</section>

<section class="slide icon-columns" style="top:2645px;left:635px">
  <h2 class="title">Lorem ipsum dolor sit</h2>
  <p class="subtitle">Your great subtitle <em>goes here</em></p>
  <div class="dots"><i></i><i></i><i></i></div>
  <p class="copy abs" style="top:82px;left:25px;width:105px">Lorem ipsum dolor sit amet, consectetur adipiscing elit, sed do eiusmod tempor incididunt ut labore et dolore magna aliqua.</p>
  <p class="copy abs" style="top:82px;left:145px;width:105px">Lorem ipsum dolor sit amet, consectetur adipiscing elit, sed do eiusmod tempor incididunt ut labore et dolore magna aliqua.</p>
  <p class="copy abs" style="top:82px;left:265px;width:105px">Lorem ipsum dolor sit amet, consectetur adipiscing elit, sed do eiusmod tempor incididunt ut labore et dolore magna aliqua.</p>
  <p class="copy abs" style="top:82px;left:385px;width:105px">Lorem ipsum dolor sit amet, consectetur adipiscing elit, sed do eiusmod tempor incididunt ut labore et dolore magna aliqua.</p>
  <div class="abs" style="top:160px;left:15px;width:120px;height:3px;background:var(--blue)"></div>
  <div class="abs" style="top:160px;left:135px;width:120px;height:3px;background:var(--orange)"></div>
  <div class="abs" style="top:160px;left:255px;width:120px;height:3px;background:var(--blue)"></div>
  <div class="abs" style="top:160px;left:375px;width:130px;height:3px;background:var(--orange)"></div>
  <svg class="abs" style="top:176px;left:60px" width="24" height="24" viewBox="0 0 24 24"><circle cx="12" cy="12" r="11" fill="var(--blue)"/><ellipse cx="12" cy="12" rx="7" ry="4" fill="#fff"/><circle cx="12" cy="12" r="2.2" fill="var(--blue)"/></svg>
  <svg class="abs" style="top:176px;left:180px" width="24" height="24" viewBox="0 0 24 24"><circle cx="12" cy="12" r="11" fill="var(--orange)"/><circle cx="12" cy="12" r="5" fill="none" stroke="#fff" stroke-width="2"/></svg>
  <svg class="abs" style="top:176px;left:300px" width="24" height="24" viewBox="0 0 24 24"><circle cx="12" cy="12" r="11" fill="var(--blue)"/><circle cx="11" cy="11" r="4" fill="none" stroke="#fff" stroke-width="2"/><path d="M14 14l4 4" stroke="#fff" stroke-width="2"/></svg>
  <svg class="abs" style="top:176px;left:425px" width="24" height="24" viewBox="0 0 24 24"><circle cx="12" cy="12" r="11" fill="var(--orange)"/><path d="M8 17v-4M12 17V8M16 17v-6" stroke="#fff" stroke-width="2"/></svg>
  <p class="abs" style="top:210px;left:35px;width:75px;text-align:center;font-size:10px;font-weight:600;color:var(--blue);text-decoration:underline">Lorem ipsum</p>
  <p class="abs" style="top:210px;left:155px;width:75px;text-align:center;font-size:10px;font-weight:600;color:var(--orange);text-decoration:underline">Lorem ipsum</p>
  <p class="abs" style="top:210px;left:275px;width:75px;text-align:center;font-size:10px;font-weight:600;color:var(--blue);text-decoration:underline">Lorem ipsum</p>
  <p class="abs" style="top:210px;left:400px;width:75px;text-align:center;font-size:10px;font-weight:600;color:var(--orange);text-decoration:underline">Lorem ipsum</p>
</section>

<section class="slide contact" style="top:2958px;left:45px">
  <h2 class="abs" style="top:55px;left:0;width:100%;text-align:center;font-size:21px;font-weight:700;color:var(--brown)">Contact Us</h2>
  <div class="abs" style="top:84px;left:0;width:100%;display:flex;justify-content:center;gap:3px"><i style="width:4px;height:4px;border-radius:50%;background:var(--orange)"></i><i style="width:4px;height:4px;border-radius:50%;background:var(--orange)"></i><i style="width:4px;height:4px;border-radius:50%;background:var(--orange)"></i></div>
  <div class="contact-item" style="top:122px;left:15px"><div class="dot" style="background:var(--sky)"></div><p>CHATTERNAME</p></div>
  <div class="contact-item" style="top:122px;left:140px"><div class="dot" style="background:var(--blue)"></div><p>PAGENAME</p></div>
  <div class="contact-item" style="top:122px;left:265px"><div class="dot" style="background:var(--orange)"></div><p>PHOTONAME</p></div>
  <div class="contact-item" style="top:122px;left:390px"><div class="dot" style="background:var(--brown)"></div><p>NETWORKNAME</p></div>
  <div class="info-item" style="top:200px;left:30px"><svg viewBox="0 0 12 12"><path d="M6 11S2 7 2 4.5a4 4 0 018 0C10 7 6 11 6 11z" fill="#444"/></svg>Your address</div>
  <div class="info-item" style="top:200px;left:140px"><svg viewBox="0 0 12 12"><path d="M3 1l2 3-1 1c1 2 2 3 3 3l1-1 3 2-1 2C5 11 1 7 1 2z" fill="#444"/></svg>000-000-0000</div>
  <div class="info-item" style="top:200px;left:255px"><svg viewBox="0 0 12 12"><circle cx="6" cy="6" r="5" fill="none" stroke="#444"/><path d="M1 6h10M6 1c-2 3-2 7 0 10M6 1c2 3 2 7 0 10" fill="none" stroke="#444"/></svg>northfielddev.example</div>
  <div class="info-item" style="top:200px;left:370px;width:110px"><svg viewBox="0 0 12 12"><rect x="1" y="2.5" width="10" height="7" fill="none" stroke="#444"/><path d="M1 3l5 4 5-4" fill="none" stroke="#444"/></svg>hello@northfielddev.example</div>
  <div class="foot-brand"><span class="foot-mark"></span><span class="foot-name">Northfield DevWorks</span></div>
  <div class="foot-rule"></div>
  <svg class="foot-home" viewBox="0 0 12 11"><path d="M0 5L6 0l6 5v6H0z" fill="var(--brown)"/></svg>
</section>

<section class="slide gears" style="top:2958px;left:635px">
  <h2 class="title">Lorem ipsum dolor sit</h2>
  <p class="subtitle">Your great subtitle <em>goes here</em></p>
  <div class="dots"><i></i><i></i><i></i></div>
  <p class="copy abs" style="top:70px;left:25px;width:110px;text-align:center">Lorem ipsum dolor sit amet, consectetur adipiscing elit, sed do eiusmod tempor incididunt ut labore et dolore magna aliqua.</p>
  <p class="copy abs" style="top:70px;left:255px;width:110px;text-align:center">Lorem ipsum dolor sit amet, consectetur adipiscing elit, sed do eiusmod tempor incididunt ut labore et dolore magna aliqua.</p>
  <p class="copy abs" style="top:70px;left:380px;width:110px;text-align:center">Lorem ipsum dolor sit amet, consectetur adipiscing elit, sed do eiusmod tempor incididunt ut labore et dolore magna aliqua.</p>
  <div class="gear-spot" role="img" aria-label="Orange gear ring ornament with a small icon" style="left:48px;background:var(--orange)"></div>
  <div class="gear-spot" role="img" aria-label="Brown gear ring ornament with a small icon" style="left:168px;background:var(--brown)"></div>
  <div class="gear-spot" role="img" aria-label="Orange gear ring ornament with a small icon" style="left:288px;background:var(--orange)"></div>
  <div class="gear-spot" role="img" aria-label="Brown gear ring ornament with a small icon" style="left:408px;background:var(--brown)"></div>
  <p class="copy abs" style="top:232px;left:145px;width:110px;text-align:center">Lorem ipsum dolor sit amet, consectetur adipiscing elit, sed do eiusmod tempor incididunt ut labore.</p>
  <div class="foot-brand"><span class="foot-mark"></span><span class="foot-name">Northfield DevWorks</span></div>
  <svg class="foot-home" viewBox="0 0 12 11"><path d="M0 5L6 0l6 5v6H0z" fill="var(--brown)"/></svg>
</section>

<section class="slide thank-you" style="top:3262px;left:340px">
  <div class="abs" style="top:22px;left:0;width:100%;display:flex;justify-content:center;align-items:center;gap:5px">
    <span style="width:11px;height:11px;border-radius:50%;border:2px solid var(--brown)"></span>
    <span style="font-size:9px;font-weight:700;color:var(--brown)">Northfield DevWorks</span>
  </div>
  <h2 class="abs" style="top:40px;left:0;width:100%;text-align:center;font-size:20px;font-weight:700;color:var(--orange)">THANK YOU</h2>
  <div class="abs" style="top:68px;left:175px;width:170px;height:1px;background:var(--line)"></div>
  <div class="contact-item" style="top:82px;left:115px"><div class="dot" style="background:var(--sky)"></div><p>CHATTERNAME</p></div>
  <div class="contact-item" style="top:82px;left:305px"><div class="dot" style="background:var(--blue)"></div><p>PAGENAME</p></div>
  <div class="contact-item" style="top:162px;left:115px"><div class="dot" style="background:var(--orange)"></div><p>PHOTONAME</p></div>
  <div class="contact-item" style="top:162px;left:305px"><div class="dot" style="background:var(--brown)"></div><p>NETWORKNAME</p></div>
</section>

</body>
</html>
```